Ferncrest Dental, LLC business card project

Business card to be designed with current logo.
Dental office- please keep design of card that looks clean and professional.
Please include the following info:
Ferncrest Dental, LLC
Dr. Lorna Pettigrew
2871 Marlowe Street
Bethlehem, PA 18093
610-555-0193
ferncrestdental.office@examplemail.test
Hello everyone-
Reason: Just got back from overseas- will look at all designs and provide feedback. Thank you!
Reason: Polling my friends for the final selection-
thank you to all those that participated- so many talented designers!

```html
<!DOCTYPE html>
<html lang="en">
<head>
<meta charset="utf-8">
<title>Ferncrest Dental, LLC — Business Card</title>
<link rel="stylesheet" href="https://fonts.googleapis.com/css2?family=Source+Sans+3:wght@300;400;700&display=swap">
<style>
  :root {
    --page-bg: #e8eae5;
    --green-deep: #5f9338;
    --green-mid: #7fae3a;
    --green-bright: #b3d63c;
    --lime: #a9c92d;
    --lime-light: #c4dc4f;
    --name-green: #5c9d30;
    --logo-green: #7cb53a;
    --ink: #2f3a2a;
    --card-white: #ffffff;
    --card-grey: #eef0ee;
    --art-grey: #e3e5e3;
  }
  * { margin: 0; padding: 0; box-sizing: border-box; }
  html, body {
    width: 1200px; height: 840px; overflow: hidden;
    background: var(--page-bg);
    font-family: "Source Sans 3", sans-serif;
  }
  .canvas { position: relative; width: 1200px; height: 840px; }

  .card {
    position: absolute;
    width: 640px; height: 366px;
    border-radius: 26px;
    overflow: hidden;
    box-shadow: 0 10px 28px rgba(40, 50, 35, 0.22);
  }

  /* Back side */
  .card-back {
    left: 60px; top: 50px;
    background: radial-gradient(ellipse at 48% 42%, var(--green-bright) 0%, var(--green-mid) 45%, var(--green-deep) 100%);
    display: flex; align-items: center; justify-content: center;
  }
  .card-back .brand { color: #ffffff; font-size: 50px; }

  .brand {
    display: flex; align-items: center; gap: 14px;
    font-weight: 300; letter-spacing: 0.5px; white-space: nowrap;
  }
  .brand-dot {
    width: 22px; height: 22px; border-radius: 50%;
    background: currentColor;
  }

  /* Front side */
  .card-front {
    left: 500px; top: 424px;
    background: radial-gradient(ellipse at 55% 30%, var(--card-white) 0%, var(--card-grey) 100%);
  }
  .card-front .brand {
    position: absolute; left: 48px; top: 40px;
    color: var(--logo-green); font-size: 44px;
  }
  .hill-art {
    position: absolute; right: 40px; top: 112px;
    width: 160px; height: 118px; border-radius: 16px;
    background: linear-gradient(180deg, var(--art-grey) 0%, var(--lime-light) 100%);
    opacity: 0.7;
  }
  .wave { position: absolute; left: 0; top: 0; width: 640px; height: 366px; }

  .doctor-name {
    position: absolute; left: 72px; top: 180px;
    color: var(--name-green); font-size: 31px; font-weight: 700;
  }
  .contact {
    position: absolute; left: 72px; top: 232px;
    list-style: none; color: var(--ink); font-size: 17px; line-height: 26px;
  }
  .contact li { display: flex; align-items: center; gap: 12px; white-space: nowrap; }
  .contact svg { width: 22px; height: 18px; flex: none; }

  .address {
    position: absolute; right: 34px; bottom: 26px;
    color: var(--ink); font-size: 17px; font-weight: 400; white-space: nowrap;
  }
</style>
</head>
<body>
<main class="canvas">

  <section class="card card-back" aria-label="Card back">
    <div class="brand"><span class="brand-dot"></span>Ferncrest Dental, LLC</div>
  </section>

  <section class="card card-front" aria-label="Card front">
    <div class="hill-art" role="img" aria-label="Illustration of a large tooth beside two trees on a green hill"></div>

    <svg class="wave" viewBox="0 0 640 366" aria-hidden="true">
      <defs>
        <linearGradient id="band" x1="0" y1="1" x2="1" y2="0">
          <stop offset="0" stop-color="var(--lime-light)"/>
          <stop offset="1" stop-color="var(--lime)"/>
        </linearGradient>
      </defs>
      <path d="M0 318 C 200 338, 370 300, 460 256 C 520 228, 580 214, 640 212 L640 366 L0 366 Z" fill="url(#band)"/>
    </svg>

    <div class="brand"><span class="brand-dot"></span>Ferncrest Dental, LLC</div>

    <h1 class="doctor-name">Dr. Lorna Pettigrew</h1>

    <ul class="contact">
      <li>
        <svg viewBox="0 0 22 18" aria-hidden="true">
          <path d="M2 6 C 6 1, 16 1, 20 6 L17 8 L15 5 H7 L5 8 Z" fill="var(--name-green)"/>
          <rect x="5" y="9" width="12" height="8" rx="2" fill="var(--name-green)"/>
          <circle cx="11" cy="13" r="2" fill="#ffffff"/>
        </svg>
        610-555-0193
      </li>
      <li>
        <svg viewBox="0 0 22 18" aria-hidden="true">
          <rect x="1" y="3" width="20" height="13" rx="1.5" fill="var(--name-green)"/>
          <path d="M2 4 L11 11 L20 4" fill="none" stroke="#ffffff" stroke-width="1.4"/>
        </svg>
        ferncrestdental.office@examplemail.test
      </li>
    </ul>

    <p class="address">2871 Marlowe Street, Bethlehem, PA 18093</p>
  </section>

</main>
</body>
</html>
```